Fallow Crest Bourbon Barrel Aged Wine

We are taking a sweet red wine and barrel aging it in previously used bourbon barrels. The abv is 16%. Kentucky based. I have attached our Brand logo for reference. Use colors that evoke warmth, richness, and sophistication. We would like to consider a raised or textured label.

Target Market(s)

bourbon and wine drinkers

```html
<!DOCTYPE html>
<html lang="en">
<head>
<meta charset="utf-8">
<title>Fallow Crest Distillery — Bourbon Barrel Aged Wine Label</title>
<link rel="stylesheet" href="https://fonts.googleapis.com/css2?family=Marcellus&display=swap">
<style>
  :root {
    --canvas-bg: #ffffff;
    --label-black: #231f20;
    --label-gold: #e8d825;
    --label-red: #c6230e;
    --label-ink: #ffffff;
  }
  html, body {
    margin: 0;
    padding: 0;
    width: 1200px;
    height: 1200px;
    overflow: hidden;
    background: var(--canvas-bg);
  }
  .canvas {
    position: relative;
    width: 1200px;
    height: 1200px;
  }
  .wine-label {
    position: absolute;
    left: 257px;
    top: 150px;
    width: 685px;
    height: 900px;
    display: block;
  }
  .band-top { fill: var(--label-black); }
  .band-chevron { fill: var(--label-gold); }
  .band-bottom { fill: var(--label-red); }
  .brand-name,
  .brand-sub,
  .wine-title,
  .style-line,
  .abv-line {
    font-family: "Marcellus", serif;
    fill: var(--label-ink);
    text-anchor: middle;
  }
  .brand-name { font-size: 42px; letter-spacing: 1px; }
  .brand-sub { font-size: 22px; letter-spacing: 4px; }
  .wine-title { font-size: 146px; letter-spacing: 2px; }
  .style-line { font-size: 34px; letter-spacing: 2px; }
  .abv-line { font-size: 34px; letter-spacing: 3px; }
</style>
</head>
<body>
  <main class="canvas">
    <svg class="wine-label" viewBox="0 0 685 900" xmlns="http://www.w3.org/2000/svg" role="group" aria-label="Fallow Crest Distillery bourbon barrel aged sweet red wine label">
      <rect class="band-top" x="0" y="0" width="685" height="900"/>
      <polygon class="band-chevron" points="0,294 342,396 685,294 685,900 0,900"/>
      <polygon class="band-bottom" points="0,321 342,421 685,321 685,900 0,900"/>

      <text class="brand-name" x="342" y="241">FALLOW CREST</text>
      <text class="brand-sub" x="342" y="267">DISTILLERY</text>

      <text class="wine-title" x="342" y="620">WINE</text>
      <text class="style-line" x="342" y="749">BOURBON BARREL AGED</text>
      <text class="abv-line" x="342" y="793">SWEET RED · 16% ABV</text>
    </svg>
  </main>
</body>
</html>
```